Floral Design for Floral Design & Events

I create floral designs for Floral Design & Events. I create unusual designs that people will remember.

Industry/Entity Type

Floral

Contact Information for Business Card

Petals
Floral Design & Events
Marlene Hayward, owner/designer
3718 Delwood Ct
Linden Vale, CA 95214
marlenehaywardq@mailvista.net
530 555-0172

Requirements
Must have
• I would like the name of the business, PETALS, to Stand Out!! I like clean, bold lines.. nothing foo-foo! Must be easy to read I'm looking for a design that catches your eye and represents my creativity. I want my card to show the potential customer that I'm unique and creative
Nice to have
• I'm thinking of the name PETALS maybe worked into the design... I'm open to your creative ideas!!!! The name must be very legible
Should not have
• I'm open to any colors other that pink and yellow..nothing Foo-Foo or flowery..

```html
<!DOCTYPE html>
<html lang="en">
<head>
<meta charset="utf-8">
<title>Petals – Floral Design &amp; Events – Business Card</title>
<link rel="stylesheet" href="https://fonts.googleapis.com/css2?family=Quicksand:wght@500;700&display=swap">
<style>
  :root {
    --backdrop: #3b3b3d;
    --card-dark: #1d1d1e;
    --card-light: #ffffff;
    --gold: #a27a35;
    --gold-light: #c39a52;
    --gold-deep: #7f5c22;
  }
  * { margin: 0; padding: 0; box-sizing: border-box; }
  html, body {
    width: 1200px; height: 720px; overflow: hidden;
    background: var(--backdrop);
  }
  .canvas { position: relative; width: 1200px; height: 720px; }

  .card {
    position: absolute; top: 205px;
    width: 540px; height: 309px;
    overflow: hidden;
    box-shadow: 0 10px 28px rgba(0,0,0,.35);
  }
  .card--front { left: 40px; background: var(--card-dark); }
  .card--back  { left: 620px; background: var(--card-light); }

  .brand {
    position: absolute; display: flex; flex-direction: column;
    align-items: center; color: var(--gold);
    font-family: "Quicksand", sans-serif;
  }
  .brand__ornament {
    display: block; border-radius: 40px;
    background: linear-gradient(90deg, var(--gold-deep), var(--gold-light) 50%, var(--gold-deep));
    opacity: .85;
  }
  .brand__name {
    display: flex; align-items: center;
    font-weight: 700; line-height: 1; color: var(--gold);
  }
  .brand__dot { border-radius: 50%; background: var(--gold); flex: none; }
  .brand__tagline { font-weight: 500; color: var(--gold); }

  /* front */
  .card--front .brand { left: 110px; top: 40px; width: 320px; }
  .card--front .brand__ornament { width: 230px; height: 30px; }
  .card--front .brand__name { font-size: 72px; gap: 14px; margin-top: 22px; }
  .card--front .brand__dot { width: 14px; height: 14px; }
  .card--front .brand__tagline { font-size: 19px; margin: 10px 0 22px; }

  /* back */
  .card--back .brand { left: 28px; top: 26px; width: 220px; }
  .card--back .brand__ornament { width: 150px; height: 20px; }
  .card--back .brand__name { font-size: 44px; gap: 9px; margin-top: 14px; }
  .card--back .brand__dot { width: 9px; height: 9px; }
  .card--back .brand__tagline { font-size: 13px; margin: 7px 0 14px; }

  .address {
    position: absolute; left: 30px; top: 232px;
    font-family: "Quicksand", sans-serif; font-style: normal; font-weight: 700;
    font-size: 15px; line-height: 1.45; color: var(--gold);
  }
  .contact {
    position: absolute; right: 36px; top: 178px; text-align: right;
    font-family: "Quicksand", sans-serif; color: var(--gold);
  }
  .contact__name { font-weight: 700; font-size: 22px; }
  .contact__role { font-weight: 500; font-size: 15px; margin-bottom: 10px; }
  .contact__line {
    display: flex; justify-content: flex-end; align-items: center; gap: 7px;
    font-weight: 500; font-size: 14px; line-height: 1.6;
  }
  .contact__icon { width: 13px; height: 13px; flex: none; }
</style>
</head>
<body>
<main class="canvas">

  <section class="card card--front" aria-label="Card front">
    <div class="brand">
      <span class="brand__ornament" role="img" aria-label="Gold filigree scroll ornament"></span>
      <div class="brand__name"><span class="brand__dot"></span>Petals</div>
      <div class="brand__tagline">Floral Design &amp; Events</div>
      <span class="brand__ornament" role="img" aria-label="Gold filigree scroll ornament"></span>
    </div>
  </section>

  <section class="card card--back" aria-label="Card back">
    <div class="brand">
      <span class="brand__ornament" role="img" aria-label="Gold filigree scroll ornament"></span>
      <div class="brand__name"><span class="brand__dot"></span>Petals</div>
      <div class="brand__tagline">Floral Design &amp; Events</div>
      <span class="brand__ornament" role="img" aria-label="Gold filigree scroll ornament"></span>
    </div>

    <address class="address">
      3718 Delwood Ct Linden Vale,<br>CA 95214
    </address>

    <div class="contact">
      <div class="contact__name">Marlene Hayward</div>
      <div class="contact__role">owner / designer</div>
      <div class="contact__line">530 555-0172
        <svg class="contact__icon" viewBox="0 0 13 13" aria-hidden="true">
          <rect x="3.5" y="1" width="6" height="11" rx="1" fill="none" stroke="currentColor" stroke-width="1.2"/>
          <rect x="5" y="3" width="3" height="4" fill="currentColor"/>
        </svg>
      </div>
      <div class="contact__line">marlenehaywardq@mailvista.net
        <svg class="contact__icon" viewBox="0 0 13 13" aria-hidden="true">
          <rect x="1" y="3" width="11" height="8" fill="none" stroke="currentColor" stroke-width="1.2"/>
          <path d="M1 3 L6.5 7.5 L12 3 M1 11 L5 6.5 M12 11 L8 6.5" fill="none" stroke="currentColor" stroke-width="1"/>
        </svg>
      </div>
    </div>
  </section>

</main>
</body>
</html>
```